A Leisure SPA Plaza Hotel needs Creative VIP Cards Design

We need VIP Cards Design for a SPA Plaza Hotel, This leisure SPA plaza hotel have multiple sub projects, such as leisure hotel room, large buffet restaurant, swimming pool, theatrical performances, sauna bath, massage, SPA, Tea bar, 3D cinema, KTV rooms, chess room, Internet cafes , art appreciation, children's Castle, Korean geothermal, table tennis, billiard room, GYM and other entertainments.
We need Three creative VIP Card design for 3 different level:
1. Golden Card
2. Platinum Card
3. Diamond Card
Attached, Please find the LOGO file and some sample, we new design with much better look than those samples.

```html
<!DOCTYPE html>
<html lang="en">
<head>
<meta charset="utf-8">
<title>VIP Cards – Seabreeze Leisure Plaza</title>
<link rel="stylesheet" href="https://fonts.googleapis.com/css2?family=Archivo+Black&display=swap">
<style>
  :root {
    --page-bg: #ececec;
    --card-black: #000000;
    --gold-band: #eea80f;
    --gold-name: #fff25a;
    --platinum-band: #c6c6c6;
    --platinum-name: #ffffff;
    --diamond-band: #88d2e8;
    --diamond-name: #ffffff;
    --ribbon-dark: rgba(0, 0, 0, 0.35);
    --ribbon-light: rgba(255, 255, 255, 0.18);
  }
  * { margin: 0; padding: 0; box-sizing: border-box; }
  html, body {
    width: 1200px;
    height: 640px;
    overflow: hidden;
    background: var(--page-bg);
  }
  .card-row {
    position: relative;
    width: 1200px;
    height: 640px;
  }
  .vip-card {
    position: absolute;
    top: 202px;
    width: 364px;
    height: 220px;
    border-radius: 9px;
    overflow: hidden;
    background: var(--card-black);
    box-shadow: 0 2px 6px rgba(0, 0, 0, 0.35);
  }
  .vip-card--gold { left: 36px; }
  .vip-card--platinum { left: 419px; }
  .vip-card--diamond { left: 802px; }
  .vip-card svg { display: block; width: 100%; height: 100%; }
  .tier-word, .vip-word {
    font-family: "Archivo Black", "Arial Black", sans-serif;
  }
  .plaza-name {
    font-family: "Archivo Black", "Arial Black", sans-serif;
    font-size: 10px;
  }
  .vip-card--gold .band { fill: var(--gold-band); }
  .vip-card--gold .plaza-name, .vip-card--gold .plaza-dot { fill: var(--gold-name); }
  .vip-card--platinum .band { fill: var(--platinum-band); }
  .vip-card--platinum .plaza-name, .vip-card--platinum .plaza-dot { fill: var(--platinum-name); }
  .vip-card--diamond .band { fill: var(--diamond-band); }
  .vip-card--diamond .plaza-name, .vip-card--diamond .plaza-dot { fill: var(--diamond-name); }
  .ribbon-dark { fill: var(--ribbon-dark); }
  .ribbon-light { fill: var(--ribbon-light); }
</style>
</head>
<body>
<main class="card-row">

  <article class="vip-card vip-card--gold">
    <svg viewBox="0 0 364 220" aria-label="Golden VIP card">
      <defs>
        <linearGradient id="gold-metal" x1="0" y1="0" x2="0" y2="1">
          <stop offset="0" stop-color="#fff6b0"/>
          <stop offset="0.45" stop-color="#f2c21c"/>
          <stop offset="0.6" stop-color="#b57a00"/>
          <stop offset="1" stop-color="#f5cf3a"/>
        </linearGradient>
      </defs>
      <path class="ribbon-light" d="M0 150 C 100 175, 220 150, 364 118 L364 140 C 220 168, 100 190, 0 170 Z"/>
      <path class="ribbon-dark" d="M0 165 C 110 195, 230 165, 364 128 L364 150 C 220 178, 100 205, 0 185 Z"/>
      <path class="band" d="M0 192 C 100 206, 230 170, 364 138 L364 220 L0 220 Z"/>
      <text class="tier-word" x="2" y="62" font-size="66" textLength="360" lengthAdjust="spacingAndGlyphs" fill="url(#gold-metal)">GOLDEN</text>
      <polygon role="img" aria-label="Metallic gold star emblem" fill="url(#gold-metal)"
        points="58,50 72.1,88.6 113.2,90.1 80.8,115.4 92.1,154.9 58,132 23.9,154.9 35.2,115.4 2.8,90.1 43.9,88.6"/>
      <text class="vip-word" x="108" y="106" font-size="54" textLength="120" lengthAdjust="spacingAndGlyphs" fill="url(#gold-metal)">VIP</text>
      <circle class="plaza-dot" cx="293" cy="180" r="9"/>
      <text class="plaza-name" x="352" y="206" text-anchor="end">Seabreeze Leisure Plaza</text>
    </svg>
  </article>

  <article class="vip-card vip-card--platinum">
    <svg viewBox="0 0 364 220" aria-label="Platinum VIP card">
      <defs>
        <linearGradient id="platinum-metal" x1="0" y1="0" x2="0" y2="1">
          <stop offset="0" stop-color="#ffffff"/>
          <stop offset="0.45" stop-color="#cfcfcf"/>
          <stop offset="0.6" stop-color="#6e6e6e"/>
          <stop offset="1" stop-color="#e2e2e2"/>
        </linearGradient>
      </defs>
      <path class="ribbon-light" d="M0 150 C 100 175, 220 150, 364 118 L364 140 C 220 168, 100 190, 0 170 Z"/>
      <path class="ribbon-dark" d="M0 165 C 110 195, 230 165, 364 128 L364 150 C 220 178, 100 205, 0 185 Z"/>
      <path class="band" d="M0 192 C 100 206, 230 170, 364 138 L364 220 L0 220 Z"/>
      <text class="tier-word" x="2" y="62" font-size="66" textLength="360" lengthAdjust="spacingAndGlyphs" fill="url(#platinum-metal)">PLATINUM</text>
      <polygon role="img" aria-label="Metallic platinum star emblem" fill="url(#platinum-metal)"
        points="58,50 72.1,88.6 113.2,90.1 80.8,115.4 92.1,154.9 58,132 23.9,154.9 35.2,115.4 2.8,90.1 43.9,88.6"/>
      <text class="vip-word" x="108" y="106" font-size="54" textLength="120" lengthAdjust="spacingAndGlyphs" fill="url(#platinum-metal)">VIP</text>
      <circle class="plaza-dot" cx="293" cy="180" r="9"/>
      <text class="plaza-name" x="352" y="206" text-anchor="end">Seabreeze Leisure Plaza</text>
    </svg>
  </article>

  <article class="vip-card vip-card--diamond">
    <svg viewBox="0 0 364 220" aria-label="Diamond VIP card">
      <defs>
        <linearGradient id="diamond-metal" x1="0" y1="0" x2="0" y2="1">
          <stop offset="0" stop-color="#e8fbff"/>
          <stop offset="0.45" stop-color="#8fd3e6"/>
          <stop offset="0.6" stop-color="#2f6f80"/>
          <stop offset="1" stop-color="#a6e2f0"/>
        </linearGradient>
      </defs>
      <path class="ribbon-light" d="M0 150 C 100 175, 220 150, 364 118 L364 140 C 220 168, 100 190, 0 170 Z"/>
      <path class="ribbon-dark" d="M0 165 C 110 195, 230 165, 364 128 L364 150 C 220 178, 100 205, 0 185 Z"/>
      <path class="band" d="M0 192 C 100 206, 230 170, 364 138 L364 220 L0 220 Z"/>
      <text class="tier-word" x="2" y="62" font-size="66" textLength="360" lengthAdjust="spacingAndGlyphs" fill="url(#diamond-metal)">DIAMOND</text>
      <polygon role="img" aria-label="Metallic ice-blue star emblem" fill="url(#diamond-metal)"
        points="58,50 72.1,88.6 113.2,90.1 80.8,115.4 92.1,154.9 58,132 23.9,154.9 35.2,115.4 2.8,90.1 43.9,88.6"/>
      <text class="vip-word" x="108" y="106" font-size="54" textLength="120" lengthAdjust="spacingAndGlyphs" fill="url(#diamond-metal)">VIP</text>
      <circle class="plaza-dot" cx="293" cy="180" r="9"/>
      <text class="plaza-name" x="352" y="206" text-anchor="end">Seabreeze Leisure Plaza</text>
    </svg>
  </article>

</main>
</body>
</html>
```